Banner Ad Design job - Bramblet Mortgage - Banner Ads for Re-Marketing Campaigns

Need a banner ad for a retargeting Campaign with Velvet Reach.

We would like to incorporate our attached logo. Also would like to incorporate a call to action "Pre-Qualify for a home loan today" and a button to click. This banner is to encourage previous customers to come back to our website and submit information. It must look good on mobile and desktop.

Our website is BrambletMortgage.example

Target Market(s)

Customers Seeking a Mortgage Loan

Industry/Entity Type

Mortgage Lender

Colors

Designer to choose colors to be used in the design.

Requirements
Must have
• - We would like the same basic design in the 4 sizes below.
• - 728x90 pixels leader board
• - 300x250 medium rectangle
• - 300x600 half page
• - 600x315 chatterbook
Nice to have
• Call to action. Click button or Something to promote them to click through
Should not have
• We are Open

```html
<!DOCTYPE html>
<html lang="en">
<head>
<meta charset="utf-8">
<title>Bramblet Mortgage – Pre-Qualify Leaderboard</title>
<link href="https://fonts.googleapis.com/css2?family=Arimo:wght@400;700&display=swap" rel="stylesheet">
<style>
  :root {
    --brand-navy: #1f4e8c;
    --sky: #b9c6d0;
    --house-sand: #c9b79c;
    --house-shadow: #7f7a70;
    --beach: #a9a8a2;
    --text-light: #ffffff;
    --cta-green: #5dcc1e;
    --cta-green-dark: #48a814;
    --fade-white: #ffffff;
  }
  html, body {
    margin: 0;
    padding: 0;
    overflow: hidden;
    background: #ffffff;
  }
  .banner {
    position: relative;
    width: 1200px;
    height: 148px;
    overflow: hidden;
    font-family: "Arimo", Arial, sans-serif;
  }
  .banner__scene {
    position: absolute;
    inset: 0;
    background: linear-gradient(180deg, var(--sky) 0%, var(--house-sand) 40%, var(--house-shadow) 70%, var(--beach) 100%);
  }
  .banner__fade {
    position: absolute;
    inset: 0;
    background: linear-gradient(90deg,
      var(--fade-white) 0%,
      rgba(255,255,255,0.95) 24%,
      rgba(255,255,255,0.55) 34%,
      rgba(255,255,255,0.15) 48%,
      rgba(255,255,255,0) 60%);
  }
  .brand {
    position: absolute;
    left: 24px;
    top: 56px;
    margin: 0;
    color: var(--brand-navy);
    font-weight: 700;
    font-size: 30px;
    line-height: 36px;
    white-space: nowrap;
  }
  .headline {
    position: absolute;
    left: 425px;
    top: 14px;
    margin: 0;
    color: var(--text-light);
    font-weight: 400;
    font-size: 44px;
    line-height: 52px;
    white-space: nowrap;
    text-shadow: 0 1px 3px rgba(0,0,0,0.25);
  }
  .cta {
    position: absolute;
    left: 936px;
    top: 36px;
    width: 231px;
    height: 76px;
    border-radius: 8px;
    background: linear-gradient(180deg, var(--cta-green) 0%, var(--cta-green-dark) 100%);
    color: var(--text-light);
    font-size: 30px;
    font-weight: 400;
    display: flex;
    align-items: center;
    justify-content: center;
    text-decoration: none;
    white-space: nowrap;
  }
</style>
</head>
<body>
  <div class="banner">
    <div class="banner__scene" role="img" aria-label="Photo of beachfront homes along a sandy shore"></div>
    <div class="banner__fade"></div>

    <p class="brand">Bramblet Mortgage</p>

    <h1 class="headline">Pre-Qualify<br>for a Home loan today</h1>

    <a class="cta" href="#">Apply Online</a>
  </div>
</body>
</html>
```